Website template for Orvel Sports Massage | ||
Sports & Remedial Therapy | ||
Massage Therapy | ||
It will be www.orvel-sportsmassage.example | ||
We are a professional company, dedicated to providing a natural pain relief from muscular or joint pain/stiffness, using thousands of years old therapy – massage (amongst other techniques e.g. Muscle Energy Technique or Trigger Point Therapy), in a modern fast-paced world where many people seem to be sustaining pain/injury from prolong working with high-tech mobile devices and computers. We relieve stress and muscular pain, increase flexibility within soft tissues and induce relaxation. We treat sports injuries, improve postures, and relieve anxiety/stress through deep tissue massage and other techniques, stretching and prescribed homecare exercises. We work closely and intuitively with soft tissues (muscles, tendons, ligaments, fascia..) and not only treat the current symptoms but also investigate the actual cause of muscular imbalance to encourage optimal healing and rehabilitation. Our clients include city office workers, athletes, manual workers, pregnant clients and everyone else in between. (I will tweak it a bit more but this is what we do in a nutshell.) |
I don’t like bright coloured websites with too many images on Homepage where it takes ages to find stuff. I am looking for a clean look/design which will be really appealing and inviting. I would like to have my logo incorporated and matching colours used. I would like a small picture of me used on the Homepage along with my logo. I'm enclosing a temporary pic of me for the design. Please feel free to use also other images to see different variations... | ||
Cutting-Edge Unique/Creative Professional Futuristic Trendy Friendly Exciting Sophisticated Modern Soft Elegant Service Oriented Fun |
Nice, soft shades of blue (that go well with my logo) | ||
Nice shades of grey (that go well with my logo) | ||
Black or red in subtle doses | ||
Verdana Century Gothic |
top | ||
http://www.brindlebodywork.example | ||
http://www.pelquavent.example/ | ||
http://www.lumaverrespa.example/ | ||
I am open to different ideas and creative input. Many thanks. Additional Information: he navigation details should be as following: Home, Treatments, Prices, Our Therapists, Contact, Testimonials, Shop, FAQS, Careers I would also like a 'join us on Facebook' , 'Buy Gift Vouchers' , 'Specials' and 'Give us your Feedback' quick links somewhere on the Home page. |

```html
<!DOCTYPE html>
<html lang="en">
<head>
<meta charset="utf-8">
<title>Orvel Sports Massage</title>
<link href="https://fonts.googleapis.com/css2?family=Questrial&family=Open+Sans:wght@400;600;700&display=swap" rel="stylesheet">
<style>
:root{
  --sky-top:#5c9be0;
  --sky-mid:#9cc6ef;
  --cloud:#ffffff;
  --nav:#3f86dc;
  --nav-dark:#2c6fc4;
  --brand:#2f7fd6;
  --ink:#3a3a3a;
  --grey:#777b80;
  --light-grey:#e6e8eb;
  --red:#c0392b;
  --footer:#3e88dd;
}
*{margin:0;padding:0;box-sizing:border-box}
html,body{width:1200px;height:1025px;overflow:hidden}
body{
  position:relative;
  font-family:"Open Sans",Verdana,sans-serif;
  color:var(--ink);
  background:
    radial-gradient(ellipse 520px 260px at 140px 700px,rgba(255,255,255,.95),rgba(255,255,255,0) 70%),
    radial-gradient(ellipse 560px 300px at 1080px 640px,rgba(255,255,255,.95),rgba(255,255,255,0) 70%),
    radial-gradient(ellipse 700px 420px at 600px 560px,#fff 55%,rgba(255,255,255,0) 80%),
    radial-gradient(ellipse 420px 200px at 1100px 260px,rgba(255,255,255,.85),rgba(255,255,255,0) 70%),
    radial-gradient(ellipse 380px 200px at 120px 300px,rgba(255,255,255,.85),rgba(255,255,255,0) 70%),
    linear-gradient(180deg,var(--sky-top) 0,var(--sky-mid) 40%,#dbeaf8 70%,#fff 90%);
}
.main-nav{
  position:absolute;left:264px;top:0;width:680px;height:40px;
  background:linear-gradient(180deg,#5a9de6,var(--nav-dark));
  border-radius:0 0 6px 6px;
  display:flex;justify-content:space-around;align-items:center;
  box-shadow:0 2px 6px rgba(0,0,0,.2);
}
.main-nav a{color:#fff;text-decoration:none;font-size:14px;font-weight:600;padding:0 10px}
.brand{position:absolute;left:264px;top:100px;width:190px}
.brand-name{
  font-family:"Questrial",sans-serif;color:var(--brand);
  font-size:34px;line-height:36px;letter-spacing:-.5px;
}
.brand-mark{display:inline-block;width:14px;height:14px;border-radius:50%;background:var(--brand);margin-left:6px;vertical-align:middle}
.brand-tag{margin-top:6px;font-size:11px;color:var(--grey);font-family:"Questrial",sans-serif;letter-spacing:.5px}
.hero{
  position:absolute;left:470px;top:40px;width:570px;height:410px;
  background:radial-gradient(ellipse at 45% 45%,#e9d2bf 0,#d9b79b 30%,#f3ece6 60%,rgba(255,255,255,0) 80%);
}
.treatments{position:absolute;left:264px;top:242px;width:196px;list-style:none}
.treatments li{display:flex;align-items:center;height:86px}
.thumb{flex:none;width:96px;height:60px;border:3px solid #fff;box-shadow:0 1px 4px rgba(0,0,0,.3);background:linear-gradient(135deg,#d8b89c,#f2e6da)}
.treatments span{margin-left:12px;font-size:14px;line-height:17px;color:var(--ink);border-bottom:2px solid var(--red);padding-bottom:2px}
.call-badge{
  position:absolute;left:264px;top:674px;width:180px;height:56px;border-radius:6px;
  background:linear-gradient(180deg,#5aa2ea,var(--nav-dark));color:#fff;
  display:flex;align-items:center;padding-left:10px;gap:10px;
}
.call-badge .txt{font-size:11px;line-height:15px}
.call-badge strong{display:block;font-size:14px}
.welcome{position:absolute;left:470px;top:452px;width:470px}
.welcome h1{font-family:"Questrial",sans-serif;font-weight:400;font-size:38px;color:#2b2b2b}
.welcome h1 small{font-size:22px;color:var(--grey)}
.welcome p{font-size:10.5px;line-height:15.5px;color:#555;margin-top:12px}
.welcome p.lead{font-weight:700;color:#333}
.gallery{position:absolute;left:270px;top:745px;width:675px;height:200px;background:#fff;border:1px solid var(--light-grey)}
.gallery h2{position:absolute;left:12px;top:10px;font-size:19px;font-weight:700;color:#333}
.gallery h2 em{font-style:normal;font-weight:400;color:var(--grey)}
.gallery-rule{position:absolute;left:12px;right:200px;top:42px;border-top:1px solid var(--light-grey)}
.gallery-items{position:absolute;left:40px;top:62px;display:flex;gap:16px}
.item{width:70px}
.item .pic{width:70px;height:74px;border:2px solid #fff;box-shadow:0 1px 3px rgba(0,0,0,.3);background:linear-gradient(160deg,#cfe6c4,#8fc07e)}
.item p{font-size:8px;line-height:11px;color:#555;margin-top:6px}
.arrow{position:absolute;top:92px}
.feature{position:absolute;right:0;top:0;width:200px;height:198px;background:radial-gradient(ellipse at 60% 60%,#f0d7c4,#b8754a 55%,#f4ebe3 85%)}
.site-footer{position:absolute;left:0;top:958px;width:1200px;height:67px;background:var(--footer)}
.site-footer p{position:absolute;left:264px;top:26px;font-size:10px;color:#e8f1fb}
.site-footer nav{position:absolute;right:264px;top:26px;font-size:10px;color:#e8f1fb}
</style>
</head>
<body>
<nav class="main-nav">
  <a href="#">Home</a><a href="#">Treatments</a><a href="#">Prices</a><a href="#">Our Therapists</a><a href="#">Shop</a><a href="#">Testimonials</a><a href="#">Contact us</a>
</nav>

<div class="brand">
  <div class="brand-name">Orvel Sports Massage<span class="brand-mark"></span></div>
  <div class="brand-tag">Sports &amp; Remedial Therapy</div>
</div>

<div class="hero" role="img" aria-label="Therapist massaging a client's leg beside green candles and a daisy"></div>

<ul class="treatments">
  <li><div class="thumb" role="img" aria-label="Sports injury treatment"></div><span>Sports<br>Injuries</span></li>
  <li><div class="thumb" role="img" aria-label="Posture massage"></div><span>Improve<br>Postures</span></li>
  <li><div class="thumb" role="img" aria-label="Skin treatment"></div><span>Acne<br>Treatment</span></li>
  <li><div class="thumb" role="img" aria-label="Ayurvedic spa oils"></div><span>Ayurvedic<br>Spa</span></li>
  <li><div class="thumb" role="img" aria-label="Hot stones on a back"></div><span>Hot Stone<br>Massage</span></li>
</ul>

<div class="call-badge">
  <svg width="26" height="26" viewBox="0 0 24 24"><path fill="#fff" d="M6.6 10.8a15 15 0 0 0 6.6 6.6l2.2-2.2a1 1 0 0 1 1-.25 11.4 11.4 0 0 0 3.6.57 1 1 0 0 1 1 1V20a1 1 0 0 1-1 1A17 17 0 0 1 3 4a1 1 0 0 1 1-1h3.5a1 1 0 0 1 1 1c0 1.25.2 2.45.57 3.6a1 1 0 0 1-.25 1z"/></svg>
  <div class="txt">Call us today<strong>+000 55 010 227</strong></div>
</div>

<section class="welcome">
  <h1>Welcome, <small>our dear visitor!</small></h1>
  <p class="lead">We are a professional company, dedicated to providing a natural pain relief from muscular or joint pain/stiffness, using thousands of years old therapy – massage (amongst other techniques e.g. Muscle Energy Technique or Trigger Point Therapy), in a modern fast-paced world where many people seem to be sustaining pain/injury from prolong working with high-tech mobile devices and computers.</p>
  <p>We relieve stress and muscular pain, increase flexibility within soft tissues and induce relaxation. We treat sports injuries, improve postures, and relieve anxiety/stress through deep tissue massage and other techniques, stretching and prescribed homecare exercises.</p>
  <p>We work closely and intuitively with soft tissues (muscles, tendons, ligaments, fascia..) and not only treat the current symptoms but also investigate the actual cause of muscular imbalance to encourage optimal healing and rehabilitation. Our clients include city office workers, athletes, manual workers, pregnant clients and everyone else in between.</p>
</section>

<section class="gallery">
  <h2>PRODUCTS <em>Gallery</em></h2>
  <div class="gallery-rule"></div>
  <svg class="arrow" style="left:12px" width="14" height="20" viewBox="0 0 14 20"><path d="M11 2 3 10l8 8" fill="none" stroke="#888" stroke-width="3"/></svg>
  <div class="gallery-items">
    <div class="item"><div class="pic" role="img" aria-label="Massage oil bottles"></div><p>Aroma oil set, relaxing blend.</p></div>
    <div class="item"><div class="pic" role="img" aria-label="Spa salts"></div><p>Bath salts, calming sea blend.</p></div>
    <div class="item"><div class="pic" role="img" aria-label="Body lotion"></div><p>Body lotion, soft daily care.</p></div>
    <div class="item"><div class="pic" role="img" aria-label="Herbal products"></div><p>Herbal balm, warm muscle relief.</p></div>
    <div class="item"><div class="pic" role="img" aria-label="Spa candles"></div><p>Scented candles, evening calm set.</p></div>
  </div>
  <svg class="arrow" style="left:452px" width="14" height="20" viewBox="0 0 14 20"><path d="M3 2l8 8-8 8" fill="none" stroke="#888" stroke-width="3"/></svg>
  <div class="feature" role="img" aria-label="Relaxed spa client with flowers in her hair"></div>
</section>

<footer class="site-footer">
  <p>© 2011 Orvel Sports Massage. All Rights Reserved.</p>
  <nav>Home | Treatments | Prices | Our Therapists | Shop | Testimonials | Contact us</nav>
</footer>
</body>
</html>
```